Business card design needed

I need a business card design also to be used on fridge magnets. All the details above to be included on the card. I am a freelance book-keeper providing services to small to medium size business providing services in LEDGA including training, consulting, BAS, IAS, preparation and lodgement, superannuation, workcover. I would like a design that is easy to read a see. Something that relates to the finance industry. A design that can be used for all other marketing products.

Target Market(s)

Small business mainly sole traders - trades people

Industry/Entity Type

Marketing

Contact Information for Business Card

Keelwind Book-keeping Services Mara Finch - LEDGA Consultant BAS REGISTERED AGENT 57302916 PO Box 7318 Harbourvale East WQ 4731 0417928360

Logo Text

Keelwind Book-keeping Services

Logo styles of interest
Emblem Logo
Pictorial/Combination Logo
Abstract Logo
Character Logo

```html
<!DOCTYPE html>
<html lang="en">
<head>
<meta charset="utf-8">
<title>Keelwind Book-keeping Services – Business Card</title>
<link rel="stylesheet" href="https://fonts.googleapis.com/css2?family=Alegreya+SC:wght@400;500&family=Alegreya:wght@400;500&display=swap">
<style>
  :root {
    --page-bg: #ffffff;
    --card-dark: #160b0d;
    --accent-teal: #12b3ad;
    --accent-yellow: #f7e21c;
    --text-light: #f4f1ee;
  }
  html, body {
    margin: 0;
    padding: 0;
    width: 1200px;
    height: 900px;
    overflow: hidden;
    background: var(--page-bg);
  }
  .canvas {
    position: relative;
    width: 1200px;
    height: 900px;
  }
  .business-card {
    position: absolute;
    left: 100px;
    top: 150px;
    width: 1000px;
    height: 600px;
    background: var(--card-dark);
    display: flex;
    color: var(--text-light);
  }
  .card-content {
    flex: 1;
    display: flex;
    flex-direction: column;
    align-items: center;
    text-align: center;
    padding-top: 125px;
  }
  .business-name {
    margin: 0;
    font-family: "Alegreya SC", "Georgia", serif;
    font-size: 36px;
    font-weight: 400;
    letter-spacing: 1.5px;
    color: var(--text-light);
  }
  .person-name {
    margin: 10px 0 0;
    font-family: "Alegreya SC", "Georgia", serif;
    font-size: 32px;
    font-weight: 400;
    letter-spacing: 1.5px;
    color: var(--accent-yellow);
  }
  .contact-details {
    margin-top: 78px;
    font-family: "Alegreya", "Georgia", serif;
    font-size: 25px;
    line-height: 1.4;
    letter-spacing: 0.5px;
  }
  .contact-details p {
    margin: 0;
  }
  .contact-details .phone {
    margin-top: 12px;
    font-size: 30px;
    letter-spacing: 1px;
  }
  .initial {
    color: var(--accent-teal);
  }
  .person-name .initial {
    color: var(--accent-yellow);
  }
  .pattern-strip {
    width: 200px;
    height: 100%;
    background: linear-gradient(180deg, var(--accent-teal) 0%, #1cb8a4 50%, var(--accent-teal) 100%);
  }
</style>
</head>
<body>
  <main class="canvas">
    <article class="business-card">
      <section class="card-content">
        <h1 class="business-name"><span class="initial">K</span>eelwind <span class="initial">B</span>ook-<span class="initial">K</span>eeping <span class="initial">S</span>ervices</h1>
        <h2 class="person-name">Mara Finch</h2>
        <div class="contact-details">
          <p>LEDGA <span class="initial">C</span>onsultant</p>
          <p><span class="initial">B</span>AS <span class="initial">R</span>EGISTERED <span class="initial">A</span>GENT&nbsp; 57302916</p>
          <p>PO <span class="initial">B</span>ox 7318 <span class="initial">H</span>arbourvale <span class="initial">E</span>ast WQ 4731</p>
          <p class="phone">0417928360</p>
        </div>
      </section>
      <div class="pattern-strip" role="img" aria-label="Decorative band of overlapping yellow serif letters on teal"></div>
    </article>
  </main>
</body>
</html>
```